Vantor Medica Innovative Business Card

Stunning business card. Background will be black. Letters in gold. Modern yet simple design that is attention grabbing. QR code leading to site. Attractive primarily to males ages 30 to 50 but also to females in same age range looking for beauty and mental health products

Target Market(s)

Males in the 30-50 age demographics

Industry/Entity Type

Pharmaceuticals selling erectile dysfunction and mens health medications

Contact Information for Business Card

www.vantormedica.example; (775) BUY-KELO; info@vantormedica.example

Colors
FFC000
F8CF3A
FAE287
FDF2CF
FEFAEE

Requirements
Must have
• Black business card with gold letters.
Nice to have
• perhaps just the logo or the "R" icon by itself on one side
Should not have
• too much content so it does not look busy

```html
<!DOCTYPE html>
<html lang="en">
<head>
<meta charset="utf-8">
<title>Vantor Medica Business Card</title>
<link rel="stylesheet" href="https://fonts.googleapis.com/css2?family=Source+Sans+3:wght@400;600;700&display=swap">
<style>
  :root {
    --backdrop: #e4e4e4;
    --card: #2a2928;
    --gold: #d2ae3a;
    --gold-soft: #e0c25a;
    --shade-dark: #1a1a1a;
    --shade-light: #3a3a3a;
  }
  * { margin: 0; padding: 0; box-sizing: border-box; }
  html, body {
    width: 1200px; height: 960px; overflow: hidden;
    background: var(--backdrop);
    font-family: "Source Sans 3", sans-serif;
  }
  .canvas { position: relative; width: 1200px; height: 960px; }
  .card {
    position: absolute; left: 300px; width: 607px; height: 347px;
    background: var(--card); overflow: hidden;
  }
  .card--front { top: 108px; }
  .card--back { top: 508px; }

  .brand {
    display: flex; align-items: center; gap: 12px;
    color: var(--gold); font-weight: 700; letter-spacing: 0.04em;
    text-transform: uppercase; white-space: nowrap;
  }
  .brand__mark {
    border-radius: 50%; background: var(--gold); flex: none;
  }
  .card--front .brand {
    position: absolute; left: 50%; top: 50%;
    transform: translate(-50%, -50%);
    font-size: 44px;
  }
  .card--front .brand__mark { width: 38px; height: 38px; }
  .card--back .brand {
    position: absolute; left: 46px; top: 44px; font-size: 28px; gap: 9px;
  }
  .card--back .brand__mark { width: 22px; height: 22px; }

  .holder { position: absolute; left: 46px; top: 182px; color: var(--gold); }
  .holder__name { font-size: 19px; font-weight: 700; line-height: 1.2; }
  .holder__role { font-size: 15px; font-weight: 400; color: var(--gold-soft); margin-top: 2px; }

  .contact { position: absolute; left: 46px; top: 254px; list-style: none; color: var(--gold-soft); }
  .contact li {
    display: flex; align-items: center; gap: 6px;
    font-size: 14.5px; line-height: 20.5px;
  }
  .contact svg { width: 13px; height: 13px; flex: none; }

  .deco-disc {
    position: absolute; left: 415px; top: 62px; width: 300px; height: 300px;
    border-radius: 50%;
    background: linear-gradient(135deg, var(--shade-light), var(--shade-dark));
  }
</style>
</head>
<body>
<main class="canvas">
  <section class="card card--front">
    <div class="brand"><span class="brand__mark"></span>Vantor Medica</div>
  </section>

  <section class="card card--back">
    <div class="brand"><span class="brand__mark"></span>Vantor Medica</div>

    <div class="holder">
      <p class="holder__name">Daniel Mercer</p>
      <p class="holder__role">President</p>
    </div>

    <ul class="contact">
      <li>
        <svg viewBox="0 0 16 16" aria-hidden="true"><path fill="currentColor" d="M3.6 1.2l2.2 2.6-1.3 1.6c.9 2 2.4 3.5 4.3 4.4l1.6-1.3 2.6 2.2-1.3 2.5C6.5 13.4 2.4 9.3 1.2 3.4z"/></svg>
        (775) BUY-KELO
      </li>
      <li>
        <svg viewBox="0 0 16 16" aria-hidden="true"><rect x="1.5" y="3.5" width="13" height="9" fill="none" stroke="currentColor" stroke-width="1.5"/><path d="M1.5 3.5l6.5 5 6.5-5" fill="none" stroke="currentColor" stroke-width="1.5"/></svg>
        info@vantormedica.example
      </li>
      <li>
        <svg viewBox="0 0 16 16" aria-hidden="true"><g fill="none" stroke="currentColor" stroke-width="1.3"><circle cx="8" cy="8" r="6.3"/><ellipse cx="8" cy="8" rx="2.8" ry="6.3"/><path d="M1.7 8h12.6"/></g></svg>
        www.vantormedica.example
      </li>
    </ul>

    <div class="deco-disc" role="img" aria-label="Large dark brand emblem decoration"></div>
  </section>
</main>
</body>
</html>
```